website design Investment Fund

I am looking for a custom website that will work on desktop computer, tablet device and a cellular device. I have attached the booklet so you can get an idea of the look we are going for. Would like to use the website eventually for crowdfunding. We like the ski racer and mountain climbing designs.

Target Market(s)

Financial Services

Industry/Entity Type

Financial Service

Coding

Coded - Design and coding required

Number of Pages Required

5+ page

Font styles to use
Sans Serif

Requirements
Must have
• Must be viewable on a cell phone and tablet and desktop
Nice to have
• Contact us form

```html
<!DOCTYPE html>
<html lang="en">
<head>
<meta charset="utf-8">
<title>Ridgeline Capital II — Secured Income Fund</title>
<link href="https://fonts.googleapis.com/css2?family=Montserrat:wght@400;500;600;700;800;900&family=Raleway:wght@400;500;600&display=swap" rel="stylesheet">
<style>
:root{
  --red:#e32228;
  --blue:#1d4f9f;
  --ink:#1b1b1b;
  --grey:#5d6168;
  --snow:#eef2f6;
  --sky:#dfe7ef;
  --dark:#121214;
  --white:#ffffff;
}
*{margin:0;padding:0;box-sizing:border-box}
html,body{width:1200px;height:4268px;overflow:hidden}
body{position:relative;background:var(--white);font-family:"Raleway",sans-serif;color:var(--ink)}
.abs{position:absolute}
.photo{position:absolute}
/* header */
.site-header{position:absolute;top:0;left:0;width:1200px;height:84px;z-index:5}
.social{position:absolute;top:26px;left:96px;display:flex;gap:14px}
.social span{width:18px;height:18px;border-radius:50%;background:var(--blue)}
.brand{position:absolute;top:22px;left:336px;display:flex;align-items:center;gap:10px;font-family:"Montserrat",sans-serif;font-weight:800;font-size:20px;color:var(--red)}
.brand i{width:18px;height:18px;background:var(--red);display:block}
.nav{position:absolute;top:30px;left:660px;display:flex;gap:34px;font-family:"Montserrat",sans-serif;font-size:14px;font-weight:600;color:var(--ink)}
.nav a{color:inherit;text-decoration:none}
.nav .active{color:var(--red)}
.btn{display:inline-block;background:var(--red);color:var(--white);font-family:"Montserrat",sans-serif;font-weight:700;font-size:14px;border-radius:22px;padding:11px 26px;text-decoration:none}
.site-header .btn{position:absolute;top:20px;left:968px}
/* hero */
.hero-photo{left:0;top:0;width:1200px;height:720px;background:linear-gradient(100deg,#8fa6bd 0%,#c9d6e2 30%,#eef2f6 55%,#ffffff 75%)}
.hero-frame{left:720px;top:176px;width:420px;height:200px;border:7px solid var(--red);border-bottom:none}
.hero-copy{left:748px;top:196px;width:420px;font-family:"Montserrat",sans-serif;font-weight:900;line-height:1}
.hero-copy .l1{font-size:62px;color:var(--blue)}
.hero-copy .l2{font-size:62px;color:var(--blue)}
.hero-copy .l3{font-size:80px;color:var(--red)}
.hero-copy .sub{margin-top:10px;font-size:19px;font-weight:800;color:var(--ink);line-height:1.2}
/* snow band */
.snow{left:0;top:700px;width:1200px;height:1580px;background:linear-gradient(180deg,#e8eef4 0%,#f5f7fa 40%,#dfe6ee 100%)}
/* company */
.company{left:196px;top:690px;width:808px;height:450px;background:var(--white);text-align:center;padding:40px 60px 0}
.company h2{font-family:"Montserrat",sans-serif;font-weight:900;font-size:62px;line-height:1}
.company h3{font-family:"Raleway",sans-serif;font-weight:500;font-size:30px;letter-spacing:2px;margin-top:6px}
.company p{font-size:13px;line-height:1.6;color:var(--grey);margin-top:18px;text-align:left}
.company .btn{margin-top:22px}
/* feature blocks */
.feature-frame{border:7px solid var(--red);background:rgba(255,255,255,.85)}
.feature h2{font-family:"Montserrat",sans-serif;font-weight:900;font-size:38px;line-height:1.05;color:var(--ink)}
.feature p{font-size:13px;line-height:1.6;color:var(--grey);margin-top:18px}
/* accredited */
.wave{left:0;width:1200px}
.acc h2{font-family:"Montserrat",sans-serif;font-weight:500;font-size:36px;color:var(--ink)}
.acc h3{font-family:"Montserrat",sans-serif;font-weight:700;font-size:24px;color:var(--blue);margin-top:14px;line-height:1.2}
.acc .series{font-family:"Montserrat",sans-serif;font-weight:800;font-size:24px;margin-top:20px}
.acc .series b{color:var(--red);font-weight:500}
.acc .note{font-size:14px;color:var(--grey);margin-top:6px}
/* team */
.team{left:0;top:3040px;width:1200px;height:720px;background:#f3f3f4}
.team h2{position:absolute;top:110px;width:100%;text-align:center;font-family:"Montserrat",sans-serif;font-weight:800;font-size:40px}
.team h3{position:absolute;top:160px;width:100%;text-align:center;font-family:"Raleway",sans-serif;font-weight:500;font-size:26px;color:var(--grey);letter-spacing:1px}
.member{position:absolute;text-align:center;font-family:"Montserrat",sans-serif}
.member .name{font-size:11px;font-weight:700;color:var(--red)}
.member .role{font-size:11px;color:var(--ink)}
.member .more{font-size:10px;font-weight:800;margin-top:6px}
.tri{position:absolute}
/* footer */
.footer{left:0;top:3740px;width:1200px;height:528px;background:var(--dark);color:#d8d8d8}
.footer h4{font-family:"Montserrat",sans-serif;font-weight:700;font-size:20px;color:var(--white);margin-bottom:16px}
.footer ul{list-style:none;font-size:14px;line-height:2}
.footer .col{position:absolute;top:140px}
.f-brand{left:140px;font-size:13px;line-height:1.6}
.f-brand .brand{position:static;color:var(--white);margin-bottom:14px}
.f-brand .brand i{background:var(--red)}
.contact li{display:flex;align-items:center;gap:10px}
.contact li span{width:16px;height:16px;border-radius:50%;background:var(--red);display:inline-block}
.news input{width:190px;height:36px;border-radius:18px;border:none;background:#2a2a2e;padding:0 14px;color:#ccc;font-family:"Raleway",sans-serif}
.news .btn{margin-top:18px;padding:9px 24px}
.f-social{display:flex;gap:12px;margin-top:22px}
.f-social span{width:26px;height:26px;border-radius:50%;background:var(--white)}
.copyright{position:absolute;bottom:18px;width:100%;text-align:center;font-size:11px;color:#888}
</style>
</head>
<body>

<header class="site-header">
  <div class="social"><span></span><span></span><span></span></div>
  <div class="brand"><i></i>RIDGELINE CAPITAL II</div>
  <nav class="nav">
    <a class="active" href="#">Home</a><a href="#">About Us</a><a href="#">Travel</a><a href="#">Gallery</a><a href="#">Testimonial</a>
  </nav>
  <a class="btn" href="#">Read More</a>
</header>

<div class="photo hero-photo" role="img" aria-label="Mountain climber with backpack standing on a snowy alpine ridge"></div>
<div class="abs hero-frame"></div>
<div class="abs hero-copy">
  <div class="l1">TOTALLY</div>
  <div class="l2">COMMITTED</div>
  <div class="l3">FOCUSED</div>
  <div class="sub">ON CAPITAL PRESERVATION AND UNINTERRUPTED INCOME FOR OUR INVESTORS</div>
</div>

<div class="abs snow" role="img" aria-label="Soft snowy mountain landscape background"></div>

<section class="abs company">
  <h2>THE COMPANY—</h2>
  <h3>Arizona's Elite Boutique Lender</h3>
  <p>Ridgeline Lending &amp; Investment, Inc. is a privately held mortgage lender, asset management and advisory firm headquartered in Scottsdale, Arizona, which specializes in fast financing for distressed, transitional and fix and flip real estate projects. Our team has decades of combined experience across private lending, underwriting and portfolio management throughout Arizona and the Southwest.</p>
  <p>At Ridgeline, we've created an exceptional product focused on delivering reliable, monthly income to investors while maintaining a conservative loan-to-value profile, disciplined underwriting standards and transparent reporting for every participant in the fund.</p>
  <p>We're proud of the incomparable personal service each of our investors experiences, and we look forward to growing alongside you.</p>
  <a class="btn" href="#">Read More</a>
</section>

<div class="photo" style="left:96px;top:1372px;width:432px;height:306px;background:linear-gradient(135deg,#c9ced5,#8d939c 55%,#e6e8eb)" role="img" aria-label="Hands typing on a laptop next to paperwork"></div>
<section class="abs feature feature-frame" style="left:570px;top:1388px;width:538px;height:320px;padding:34px 40px">
  <h2>THE BOUTIQUE FUND<br>INVESTORS ARE<br>LOOKING FOR</h2>
  <p>As an Arizona boutique fund, we offer investors a focused, relationship driven approach. We provide short term loans secured by first position real estate, with conservative leverage, careful borrower selection and monthly distributions paid directly to our investors.</p>
</section>

<section class="abs feature feature-frame" style="left:90px;top:1800px;width:540px;height:320px;padding:40px 40px">
  <h2>INVESTMENT STRATEGY:</h2>
  <p>The fund manager has decades of experience in private lending, real estate and portfolio management. Our strategy is to preserve capital while generating consistent income by originating well secured loans, actively managing each position and maintaining strict underwriting standards throughout the life of every investment in the fund.</p>
</section>
<div class="photo" style="left:676px;top:1762px;width:432px;height:334px;background:linear-gradient(135deg,#3c3f46,#9fb3c9 50%,#e3e7ec)" role="img" aria-label="Laptop displaying financial charts on a desk"></div>

<svg class="abs wave" style="top:2180px" width="1200" height="140" viewBox="0 0 1200 140" aria-hidden="true">
  <path d="M0 40 Q300 140 600 90 T1200 70 V140 H0Z" fill="#ffffff"/>
  <path d="M0 40 Q300 140 600 90 T1200 70" fill="none" stroke="var(--blue)" stroke-width="6"/>
</svg>

<div class="photo" style="left:94px;top:2370px;width:378px;height:270px;background:linear-gradient(135deg,#1f2d4a,#6b7d96 55%,#c4ccd6)" role="img" aria-label="Businessman signing a contract with a pen"></div>
<section class="abs acc" style="left:560px;top:2380px;width:560px">
  <h2>ACCREDITED INVESTORS ONLY</h2>
  <h3>MINIMUM INVESTMENT<br>REQUIREMENTS</h3>
  <div class="series">SERIES A <b>$50,000 - $249,999</b></div>
  <div class="note">Rate of the return 10% a 7% per annum term 24 Month</div>
</section>

<section class="abs acc" style="left:94px;top:2690px;width:560px">
  <h2>ACCREDITED INVESTORS ONLY</h2>
  <h3>MINIMUM INVESTMENT<br>REQUIREMENTS</h3>
  <div class="series">SERIES <b>$250,000.00</b></div>
  <div class="note">Rate of the return 10% a 8% per annum term 24 Month</div>
</section>
<div class="photo" style="left:660px;top:2660px;width:350px;height:300px;background:linear-gradient(135deg,#d8dde3,#a9b4c0 55%,#f1f3f5)" role="img" aria-label="Hands holding a tablet showing financial graphs"></div>

<section class="abs team">
  <svg class="abs" style="top:-40px;left:0" width="1200" height="110" viewBox="0 0 1200 110" aria-hidden="true">
    <path d="M0 0 H1200 V40 Q900 110 600 60 T0 70Z" fill="#ffffff"/>
    <path d="M0 70 Q300 10 600 60 T1200 40" fill="none" stroke="var(--blue)" stroke-width="6"/>
  </svg>
  <h2>OUR TEAM</h2>
  <h3>FOUNDING MEMBERS AND FUND MANAGERS</h3>

  <svg class="tri" style="left:120px;top:240px" width="270" height="240" viewBox="0 0 270 240" role="img" aria-label="Portrait of founder and fund manager"><polygon points="0,0 270,0 135,240" fill="var(--red)"/><polygon points="14,8 256,8 135,222" fill="#b9bec6"/></svg>
  <div class="member" style="left:150px;top:490px;width:210px"><div class="name">MARK ELLISON</div><div class="role">Founder and Fund Manager</div><div class="more">READ MORE</div></div>

  <div class="member" style="left:400px;top:250px;width:200px"><div class="name">DANA WHITFORD</div><div class="role">Founder and Managing Partner</div><div class="more">READ MORE</div></div>
  <svg class="tri" style="left:400px;top:330px" width="200" height="190" viewBox="0 0 200 190" role="img" aria-label="Portrait of founding partner"><polygon points="100,0 200,190 0,190" fill="var(--red)"/><polygon points="100,18 186,182 14,182" fill="#d6c9bd"/></svg>

  <svg class="tri" style="left:640px;top:240px" width="230" height="210" viewBox="0 0 230 210" role="img" aria-label="Portrait of fund advisor"><polygon points="0,0 230,0 115,210" fill="var(--red)"/><polygon points="14,8 216,8 115,192" fill="#b3b8c0"/></svg>
  <div class="member" style="left:650px;top:460px;width:210px"><div class="name">TOM CALDERA</div><div class="role">Fund Advisor</div><div class="more">READ MORE</div></div>

  <div class="member" style="left:900px;top:250px;width:200px"><div class="name">JOE MARSTON</div><div class="role">Chief Investment Officer</div><div class="more">READ MORE</div></div>
  <svg class="tri" style="left:900px;top:320px" width="220" height="210" viewBox="0 0 220 210" role="img" aria-label="Portrait of chief investment officer"><polygon points="110,0 220,210 0,210" fill="var(--red)"/><polygon points="110,18 206,202 14,202" fill="#a8adb5"/></svg>
</section>

<footer class="abs footer">
  <svg class="abs" style="top:-30px;left:0" width="1200" height="70" viewBox="0 0 1200 70" aria-hidden="true">
    <path d="M0 30 Q600 -20 1200 30 V70 H0Z" fill="var(--dark)"/>
    <path d="M0 30 Q600 -20 1200 30" fill="none" stroke="var(--red)" stroke-width="6"/>
  </svg>
  <div class="col f-brand" style="top:90px">
    <div class="brand"><i></i>RIDGELINE CAPITAL II</div>
    4120 N Canyon Ridge Rd, Suite 210,<br>Scottsdale, AZ 85251<br><br>
    This document is intended as a summary of certain<br>information contained in the Ridgeline Capital II<br>Secured Income Fund.
    <div class="f-social"><span></span><span></span><span></span></div>
  </div>
  <div class="col" style="left:460px">
    <h4>Site Map</h4>
    <ul><li>Home</li><li>About Us</li><li>Travel</li><li>Gallery</li><li>Testimonial</li><li>Contact Us</li></ul>
  </div>
  <div class="col contact" style="left:650px">
    <h4>Contact Us</h4>
    <ul><li><span></span>555-014-2201</li><li><span></span>555-014-2202</li><li><span></span>555-014-2203</li><li><span></span>555-014-2204</li><li><span></span>555-014-2205</li></ul>
  </div>
  <div class="col news" style="left:870px">
    <h4>Newsletter</h4>
    <input type="text" placeholder="Email Address"><br>
    <a class="btn" href="#">Subscribe</a>
  </div>
  <div class="copyright">© Ridgeline Capital II. All Rights Reserved.</div>
</footer>

</body>
</html>
```